Korelith InsurTech Website Redesign - 10 Pages

Design a modern, professional website for Korelith, an AI-native cyber insurance platform serving SMBs.

DELIVERABLE: 10 pages (desktop + mobile mockups)
- Homepage (priority #1)
- 4 Platform pages (Cyber Insurance, Brokers, Underwriters, Policyholder)
- 3 Company pages (About Us, Team, Contact/Careers)
- 2 Risk pages (AI Risk, Cyber Risk)

DESIGN DIRECTION:
- Professional + innovative (insurance meets technology)
- Trust-building + modern aesthetic
- Reference: Brambury Insurance, Tidewick Insurance
- Use official brand colors (6-color palette provided)
- Avoid generic security clipart (padlocks, shields, magnifying glasses)
- Custom graphics, not AI-generated or stock imagery

CURRENT SITES FOR REFERENCE:
- www.korelith.ai
- https://a3c9124d.korelith-website.vorlapages.dev/

Full detailed brief with all content, page specifications, and brand guidelines attached as PDF (Korelith_PixelHarbor_Brief.pdf).

TARGET AUDIENCE: Insurance brokers (primary), SMB business owners (secondary)
KEY MESSAGE: "Cyber Insurance the Way It Should Be"

Additional brand assets available in Google Drive - link provided on request.

```html
<!DOCTYPE html>
<html lang="en">
<head>
<meta charset="utf-8">
<title>Korelith — Cyber Insurance the Way It Should Be</title>
<link rel="stylesheet" href="https://fonts.googleapis.com/css2?family=Poppins:wght@400;500;600;700&display=swap">
<style>
:root{
  --teal:#4cc3b4;
  --teal-soft:#5cd0d6;
  --ink:#1e1e24;
  --body:#3a3a42;
  --navy:#1c1f3b;
  --hero-dark:#151a4a;
  --royal:#1b1db0;
  --deep-green:#0c3f3d;
  --mist:#e5f3f3;
  --field:#e7e8f5;
  --white:#ffffff;
}
*{box-sizing:border-box;margin:0;padding:0}
html,body{width:1200px;height:4104px;overflow:hidden;background:var(--white)}
body{font-family:'Poppins',sans-serif;color:var(--ink)}
.page{position:relative;width:1200px;height:4104px;overflow:hidden}
.abs{position:absolute}
.btn{position:absolute;display:flex;align-items:center;justify-content:center;background:var(--teal);color:var(--white);font-weight:600;font-size:14px;letter-spacing:.2px;border-radius:3px}

/* header */
.site-header{position:absolute;left:0;top:0;width:1200px;height:83px;background:var(--white);z-index:5}
.brand{position:absolute;left:134px;top:20px;font-size:32px;font-weight:600;color:var(--deep-green);letter-spacing:1px;line-height:42px}
.nav{position:absolute;top:32px;font-size:14px;color:#4a4a52}
.nav-cta{left:993px;top:22px;width:127px;height:42px;font-size:15px;font-weight:500;box-shadow:0 3px 8px rgba(0,0,0,.15)}

/* hero */
.hero{position:absolute;left:0;top:83px;width:1200px;height:722px}
.hero-art{position:absolute;inset:0;background:linear-gradient(100deg,#050608 0,#050608 100px,#1a1d5a 100px,#1f2c8a 45%,#1a5fc0 65%,#0f2a78 85%,#0b1550 100%);clip-path:polygon(0 0,100% 0,100% 570px,749px 618px,100px 680px,0 690px)}
.hero-title{position:absolute;left:154px;color:var(--white);line-height:1}
.hero-title .l1{position:absolute;top:150px;font-size:58px;font-weight:400;white-space:nowrap}
.hero-title .l2{position:absolute;top:210px;font-size:58px;font-weight:700;color:var(--teal);white-space:nowrap}
.hero-title .l3{position:absolute;top:279px;font-size:31px;font-weight:400;white-space:nowrap}
.hero-sub{position:absolute;left:154px;top:336px;font-size:19px;line-height:30px;color:var(--white);white-space:nowrap}
.hero-cta{left:155px;top:512px;width:306px;height:54px;font-size:15px}
.hero-shapes{position:absolute;left:0;top:0}
.hero-dot{position:absolute;left:562px;top:594px;width:76px;height:76px;border-radius:50%;background:var(--white)}

/* partner */
.partner-title{position:absolute;left:0;width:1200px;text-align:center}
.partner-copy{position:absolute;left:240px;top:984px;width:720px;text-align:center;font-size:16px;line-height:30px;color:var(--body)}

/* services */
.services-bg{position:absolute;left:0;top:1100px}
.services-head{position:absolute;left:204px;top:1305px;font-size:46px;font-weight:700;line-height:60px}
.services-sub{position:absolute;left:204px;top:1372px;font-size:21px;font-weight:500;line-height:26px;color:#2c2c33}
.services-copy{position:absolute;left:204px;top:1443px;width:330px;font-size:16.5px;line-height:27px;color:var(--body)}
.services-cta{left:202px;top:1636px;width:283px;height:48px}
.card{position:absolute;width:215px;height:242px;background:var(--white);border-radius:8px;box-shadow:0 4px 18px rgba(20,40,60,.08);text-align:center;padding:0 16px}
.card.featured{background:var(--royal);color:var(--white)}
.card-icon{display:block;margin:28px auto 14px;width:60px;height:60px}
.card h3{font-size:16px;font-weight:600;line-height:20px}
.card p{font-size:11.5px;line-height:17px;margin-top:12px;color:#3a3a42}
.card.featured p{color:var(--white)}

/* features */
.feature-head{position:absolute;font-size:38px;font-weight:600;line-height:44px;white-space:nowrap}
.feature-head span{display:block;font-size:27px;font-weight:400;line-height:34px}
.feature-copy{position:absolute;width:330px;font-size:15px;line-height:23.5px;color:var(--body)}
.feature-cta{width:162px;height:50px;font-size:16px}
.diamond{position:absolute;width:272px;height:272px;border-radius:34px;transform:rotate(45deg)}
.diamond.frame{border:2px solid var(--teal);background:transparent}
.diamond.photo{box-shadow:0 20px 40px rgba(20,30,90,.3)}
.connector{position:absolute;height:2px;background:var(--teal)}
.connector i{position:absolute;top:-4px;width:10px;height:10px;border-radius:50%;background:var(--teal)}

/* trust band */
.band{position:absolute;left:0;top:0}
.band-art{position:absolute;left:0;top:2793px;width:1200px;height:610px;background:radial-gradient(ellipse at 62% 45%,#2c34c8 0,#1e22b0 45%,#1818a0 100%);clip-path:polygon(0 137px,100% 0,100% 475px,0 610px)}
.band-title{position:absolute;left:186px;top:2982px;color:var(--white);font-size:52px;font-weight:700;line-height:64px}
.band-sub{position:absolute;left:186px;top:3046px;color:var(--teal-soft);font-size:34px;font-weight:500;line-height:43px}
.band-cta{left:193px;top:3155px;width:154px;height:47px}
.band-right{position:absolute;left:615px;top:3012px;color:var(--white)}
.band-right h3{font-size:24px;font-weight:500;line-height:36px}
.band-right p{font-size:17px;line-height:26px;margin-top:10px;width:420px}

/* contact */
.contact-title{position:absolute;left:0;top:3394px;width:1200px;text-align:center;font-size:32px;line-height:44px}
.field{position:absolute;background:var(--field);font-size:13px;color:#3c3d55;padding:0 16px;display:flex;align-items:center}
.field.area{align-items:flex-start;padding-top:12px}
.send{left:537px;top:3669px;width:126px;height:40px;font-size:14px}

/* footer */
.footer-bg{position:absolute;left:0;top:3770px;width:1200px;height:334px;background:var(--navy);clip-path:polygon(0 32px,100% 0,100% 100%,0 100%)}
.footer-brand{position:absolute;left:160px;top:3824px;font-size:34px;font-weight:500;color:var(--white);letter-spacing:1px;line-height:44px}
.footer-phone{position:absolute;left:160px;top:3898px;font-size:16px;color:var(--white)}
.footer-note{position:absolute;left:160px;top:3926px;font-size:11.5px;line-height:18px;color:#c8cad8;width:280px}
.footer-col{position:absolute;top:3834px;color:var(--white)}
.footer-col h4{font-size:13px;font-weight:500;line-height:18px}
.footer-col li{list-style:none;font-size:12px;line-height:24.7px;color:#c8cad8}
.footer-col li:first-child{margin-top:6px}
.footer-col .note{font-size:11px;color:#c8cad8;margin-top:12px}
.sub-input{position:absolute;left:724px;top:3897px;width:216px;height:34px;background:var(--white);border-radius:17px 0 0 17px;font-size:12px;color:#8a8c99;padding-left:22px;display:flex;align-items:center}
.sub-btn{position:absolute;left:932px;top:3897px;width:107px;height:34px;background:var(--teal);border-radius:17px;color:var(--white);font-size:13px;font-weight:500;display:flex;align-items:center;justify-content:center}
.social{position:absolute;top:3981px;width:11px;height:11px;border-radius:50%;background:#b9bccb}
.footer-rule{position:absolute;left:0;top:4041px;width:1200px;height:1px;background:#34385a}
.copyright{position:absolute;left:0;top:4063px;width:1200px;text-align:center;font-size:12px;color:#c8cad8}
</style>
</head>
<body>
<div class="page">

  <header class="site-header">
    <div class="brand">korelith</div>
    <span class="nav" style="left:491px">Why korelith</span>
    <span class="nav" style="left:612px">Proven Performance</span>
    <span class="nav" style="left:773px">Trusted by Industry Leaders</span>
    <div class="btn nav-cta">Get Started</div>
  </header>

  <section class="hero">
    <div class="hero-art" role="img" aria-label="Businessman in a suit holding a glowing blue cyber insurance network hologram"></div>
    <svg class="hero-shapes" width="1200" height="722" viewBox="0 0 1200 722">
      <polygon points="749,618 1200,570 1200,666" fill="#5fd3c6"/>
      <polygon points="749,618 1200,666 1200,722" fill="#0c3f3d"/>
    </svg>
    <div class="hero-title">
      <div class="l1">Cyber</div>
      <div class="l2">Insurance</div>
      <div class="l3">the Way It Should Be</div>
    </div>
    <p class="hero-sub">Continuous risk assessment.<br>Tailored coverage. Seamless protection.</p>
    <div class="btn hero-cta">PROTECT YOUR BUSINESS TODAY</div>
    <div class="hero-dot"></div>
  </section>

  <section class="partner">
    <div class="partner-title" style="top:843px;font-size:38px;line-height:50px">Your Trusted Partner in</div>
    <div class="partner-title" style="top:895px;font-size:54px;font-weight:700;line-height:68px">Cybersecurity</div>
    <p class="partner-copy">Korelith’s commitment to safeguarding your business has earned &nbsp;us the trust of industry leaders and innovators across the globe. With continuous risk assessment and responsive policies, you gain a partner as invested in your security as you are.</p>
  </section>

  <section class="services">
    <svg class="services-bg" width="1200" height="780" viewBox="0 0 1200 780">
      <polygon points="0,110 1200,13 1200,778 0,778" fill="#e5f3f3"/>
      <line x1="0" y1="108" x2="1200" y2="11" stroke="#0c3f3d" stroke-width="5"/>
    </svg>
    <h2 class="services-head">What we do</h2>
    <p class="services-sub">Strong Protection Backed by<br>Smarter Insights</p>
    <p class="services-copy">In a rapidly evolving digital landscape, staying secure requires more than just insurance—it demands ongoing vigilance against ever-changing threats. That’s why we empower policyholders with:</p>
    <div class="btn services-cta">DISCOVER YOUR POLICY OPTIONS</div>

    <article class="card" style="left:596px;top:1250px">
      <svg class="card-icon" viewBox="0 0 60 60" fill="none" stroke="#1d5f5c" stroke-width="2"><rect x="12" y="6" width="30" height="40" rx="3"/><line x1="18" y1="30" x2="36" y2="30"/><line x1="18" y1="36" x2="30" y2="36"/><circle cx="38" cy="40" r="8"/><line x1="44" y1="46" x2="52" y2="54"/></svg>
      <h3>Continuous Risk Assessment</h3>
      <p>Korelith’s advanced, AI-native analytics monitor your cyber risk...</p>
    </article>
    <article class="card featured" style="left:827px;top:1208px">
      <svg class="card-icon" viewBox="0 0 60 60" fill="none" stroke="#ffffff" stroke-width="2"><rect x="14" y="8" width="32" height="38" rx="3"/><line x1="20" y1="32" x2="40" y2="32"/><line x1="20" y1="38" x2="34" y2="38"/><circle cx="30" cy="20" r="6"/><line x1="8" y1="50" x2="52" y2="50"/></svg>
      <h3>Tailored Policies That Work for You</h3>
      <p>Flexible solutions crafted to fit your unique needs—whether you’re a small business...</p>
    </article>
    <article class="card" style="left:596px;top:1508px">
      <svg class="card-icon" viewBox="0 0 60 60" fill="none" stroke="#1d5f5c" stroke-width="2"><polygon points="30,6 51,18 51,42 30,54 9,42 9,18"/><circle cx="30" cy="30" r="8"/></svg>
      <h3>Actionable Security Services</h3>
      <p>Specific, targeted tasks for policyholders to strengthen defense and reduce...</p>
    </article>
    <article class="card" style="left:827px;top:1466px">
      <svg class="card-icon" viewBox="0 0 60 60" fill="none" stroke="#1d5f5c" stroke-width="2"><rect x="16" y="14" width="28" height="32" rx="4"/><line x1="8" y1="22" x2="16" y2="22"/><line x1="44" y1="22" x2="52" y2="22"/><line x1="8" y1="38" x2="16" y2="38"/><line x1="44" y1="38" x2="52" y2="38"/><circle cx="30" cy="30" r="5"/></svg>
      <h3>Trusted Partner in Cybersecurity</h3>
      <p>Korelith’s commitment to safeguarding your business has earned us the trust ...</p>
    </article>
  </section>

  <section class="feature">
    <h2 class="feature-head" style="left:179px;top:1976px">Better Risk<span>Quantification Engine</span></h2>
    <p class="feature-copy" style="left:179px;top:2070px">Korelith’s AI-powered platform delivers unparalleled accuracy in risk assessment, outperforming competitors that rely on flawed data sources and outdated calculation methods.</p>
    <div class="btn feature-cta" style="left:182px;top:2214px">LEARN MORE</div>
    <div class="connector" style="left:537px;top:2143px;width:116px"><i style="left:-4px"></i></div>
    <div class="diamond frame" style="left:722px;top:1970px"></div>
    <div class="diamond photo" style="left:712px;top:1992px;background:linear-gradient(135deg,#3a66d8,#1a2a9a 55%,#0d1660)" role="img" aria-label="Hand with a stylus touching a risk management gauge dial"></div>
  </section>

  <section class="feature">
    <h2 class="feature-head" style="left:711px;top:2425px">Enhanced Value<span>for Customers</span></h2>
    <p class="feature-copy" style="left:711px;top:2518px">Korelith’s security-first platform em-powers clients to strengthen their security posture, providing lasting benefits and continuous incentives year after year.</p>
    <div class="btn feature-cta" style="left:712px;top:2664px">LEARN MORE</div>
    <div class="connector" style="left:566px;top:2507px;width:86px"><i style="right:-4px"></i></div>
    <div class="diamond frame" style="left:228px;top:2420px"></div>
    <div class="diamond photo" style="left:218px;top:2443px;background:linear-gradient(135deg,#3560d0,#1d2f9c 55%,#0c1660)" role="img" aria-label="Hand with a stylus and a value gauge arc from min to max"></div>
  </section>

  <section class="trust">
    <div class="band-art" role="img" aria-label="Deep blue world map network backdrop"></div>
    <h2 class="band-title">Trusted,</h2>
    <p class="band-sub">Dedicated, Mordern<br>Cyber Security.</p>
    <div class="btn band-cta">WHO WE ARE</div>
    <div class="band-right">
      <h3>Trusted by Industry Leaders</h3>
      <p>Korelith’s commitment to safeguarding your business has earned us the trust of industry.</p>
    </div>
  </section>

  <section class="contact">
    <h2 class="contact-title">Get in <b>Touch</b></h2>
    <div class="field" style="left:311px;top:3462px;width:279px;height:37px">Full Name</div>
    <div class="field" style="left:612px;top:3462px;width:279px;height:37px">Email</div>
    <div class="field" style="left:311px;top:3510px;width:279px;height:38px">Phone No</div>
    <div class="field" style="left:612px;top:3510px;width:279px;height:38px">Company</div>
    <div class="field area" style="left:311px;top:3559px;width:580px;height:91px">Message</div>
    <div class="btn send">SEND</div>
  </section>

  <footer>
    <div class="footer-bg"></div>
    <div class="footer-brand">korelith</div>
    <div class="footer-phone">+123 &nbsp;(555-0142)</div>
    <p class="footer-note">Reducing the frequency and severity of cyber risk by strengthening organizations’ cyber risk posture.</p>
    <div class="footer-col" style="left:510px">
      <h4>Quick Links</h4>
      <ul><li>The Problem</li><li>The Solution</li><li>How it Works</li><li>Privacy Policy</li><li>Terms and Conditions</li></ul>
    </div>
    <div class="footer-col" style="left:720px">
      <h4>WRITE TO US</h4>
      <p class="note">Provide your email below to subscribe to our newsletter</p>
      <h4 style="margin-top:66px">FOLLOW US</h4>
    </div>
    <div class="sub-input">Email address</div>
    <div class="sub-btn">Subscribe</div>
    <span class="social" style="left:728px"></span>
    <span class="social" style="left:752px"></span>
    <span class="social" style="left:776px"></span>
    <span class="social" style="left:800px"></span>
    <span class="social" style="left:824px"></span>
    <div class="footer-rule"></div>
    <div class="copyright">Copyright 2026 korelith.ai</div>
  </footer>

</div>
</body>
</html>
```